Digital Agency Needs a Relaunch

We are looking for a modern, top-notch design to elevate our brand to win new clients. It has to build on the clarity of message in the current wireframes and must fit together well on Wordpress.

The winning designer will need to complete the other pages, but please focus on the homepage as the base of your proposed designs for us.

Use the existing logo as a point, and the colour scheme should be around that, we currently use these colours, but you can suggest new mixes:
Purple: #5c306b
Orange: #e27927
Grey: #5f4f61
Light grey: #cacaca
Off white: #ececec
Blue: #674ea7
Updates

Need extra days to review

Target Market(s)

Decent Sized SME Businesses (20+ Staff, Over £1m turnover)

Industry/Entity Type

Digital Marketing

Number of Pages Required

5+ page

Font styles to use
Sans Serif

Colors

Designer to choose colors to be used in the design.

Requirements
Must have
• A real attention on the design piece. Ignore the current website and really focus on the messaging and the brief.
Nice to have
• Read the messages and think about the impact. Use the purple in the logo more than the orange, but try to keep it smart rather than cool
Should not have
• Inconsistent design, serif fonts, stock images and not meeting the wireframes.

```html
<!DOCTYPE html>
<html lang="en">
<head>
<meta charset="utf-8">
<title>Quillmere Digital – Growth works for you</title>
<link href="https://fonts.googleapis.com/css2?family=Poppins:wght@400;500;600;700&display=swap" rel="stylesheet">
<style>
:root{
  --purple:#5c306b;
  --blue:#674ea7;
  --hero:#6a4fa8;
  --band-dark:#6643a0;
  --orange:#e27927;
  --grey:#5f4f61;
  --light-grey:#cacaca;
  --off-white:#ececec;
  --ink:#2a2230;
  --text:#4a4350;
  --footer:#2e2233;
  --footer-text:#a99bb0;
}
*{box-sizing:border-box;margin:0;padding:0}
html,body{width:1200px;height:5227px;overflow:hidden}
body{font-family:'Poppins',sans-serif;color:var(--ink);background:#fff;position:relative}
.abs{position:absolute}

/* header */
.site-header{position:absolute;top:0;left:0;width:1200px;height:120px;background:#fff}
.brand{position:absolute;left:68px;top:34px;display:flex;align-items:center;gap:8px;font-size:30px;font-weight:500;color:var(--grey);letter-spacing:-.5px}
.brand .dot{width:14px;height:14px;border-radius:50%;background:var(--orange)}
.utility-nav{position:absolute;top:36px;right:66px;display:flex;font-size:11px;color:var(--ink)}
.utility-nav span{padding:0 18px;border-left:1px solid var(--light-grey);line-height:14px}
.utility-nav span:first-child{border-left:0}
.main-nav{position:absolute;top:80px;right:66px;display:flex;gap:52px;font-size:13px;font-weight:500}

/* hero */
.hero{position:absolute;top:120px;left:0;width:1200px;height:585px;background:var(--hero);overflow:hidden}
.hero h1{position:absolute;left:70px;top:165px;font-size:52px;line-height:58px;font-weight:600;color:#fff}
.hero h1 em{font-style:normal;color:#c9b8f0;display:block;margin-top:12px}
.hero-art{position:absolute;left:520px;top:40px;width:680px;height:545px;background:linear-gradient(135deg,#8a74c4 0%,#f2f0f7 55%,#e8894a 100%);clip-path:polygon(18% 30%,70% 0,100% 0,100% 100%,8% 100%)}

/* intro */
.intro-title{position:absolute;top:795px;left:0;width:1200px;text-align:center;font-size:40px;font-weight:500;line-height:58px}
.intro-title span{display:block;color:var(--purple)}
.pillar{position:absolute;top:980px;width:300px;font-size:16px;line-height:25px;color:var(--text)}
.pillar svg{display:block;margin-bottom:18px}
.pillar b{font-weight:400;color:var(--blue)}

/* orange band */
.cta-band{position:absolute;top:1285px;left:19px;width:1181px;height:100px;background:var(--orange)}
.cta-band h2{position:absolute;left:79px;top:24px;font-size:38px;font-weight:500;color:#fff}
.btn{position:absolute;background:#fff;border-radius:6px;font-size:17px;font-weight:500;color:var(--ink);display:flex;align-items:center;justify-content:center;gap:10px}

/* service cards */
.service-card{position:absolute;width:513px;height:295px;border:1px solid #ddd;border-radius:6px;background:#fff}
.service-card .accent{position:absolute;top:-1px;left:40px;width:92px;height:4px}
.service-card h3{position:absolute;left:40px;top:40px;font-size:25px;font-weight:600}
.service-item{position:absolute;display:flex;align-items:center;gap:16px;font-size:18px;color:var(--ink);line-height:21px}
.service-item i{width:26px;height:26px;border-radius:6px;flex:none}

/* pain / gain */
.showcase-top{position:absolute;top:2213px;left:0;width:1200px;height:84px;background:var(--hero)}
.tag{position:absolute;left:102px;top:30px;background:var(--purple);color:#fff;font-size:11px;font-weight:600;padding:3px 7px;border-radius:3px;letter-spacing:.5px}
.showcase{position:absolute;top:2297px;left:0;width:1200px;height:246px;background:var(--band-dark);color:#fff}
.showcase h3{position:absolute;top:48px;font-size:29px;font-weight:600}
.showcase p{position:absolute;top:104px;font-size:20px;line-height:25px}

/* about */
.about-title{position:absolute;top:2635px;left:68px;font-size:40px;font-weight:600}
.about-title span{color:var(--purple)}
.about-list{position:absolute;left:68px;top:2748px;width:570px;list-style:none}
.about-list li{display:flex;gap:18px;font-size:14px;line-height:23px;color:var(--text);margin-bottom:21px}
.about-list svg{flex:none;margin-top:3px}
.about-art{position:absolute;left:790px;top:2655px;width:400px;height:440px;background:linear-gradient(160deg,#fff 0%,#f3d6cb 35%,#d66a4e 70%,#f7e9e3 100%)}

/* case studies */
.cases{position:absolute;top:3180px;left:0;width:1200px;height:650px;background:var(--off-white)}
.cases h2{position:absolute;left:76px;top:60px;font-size:52px;line-height:62px;font-weight:600;color:var(--blue)}
.cases h2 span{display:block;color:var(--purple)}
.case-card{position:absolute;top:268px;width:252px;height:307px;background:#fff;border-radius:10px}
.case-card.is-raised{box-shadow:0 10px 18px rgba(0,0,0,.18)}
.learn{position:absolute;left:25px;bottom:28px;font-size:15px;color:var(--purple);display:flex;align-items:center;gap:8px}

/* blog */
.blog-title{position:absolute;left:76px;top:3895px;font-size:50px;font-weight:600;color:var(--grey)}
.blog-card{position:absolute;top:4005px;width:252px}
.blog-card .thumb{height:307px;border:1px solid var(--light-grey);border-radius:10px}
.blog-card h4{margin-top:22px;width:232px;font-size:19px;font-weight:500;line-height:24px;color:var(--ink)}

/* footer */
.turbo{position:absolute;top:4500px;left:0;width:1200px;height:78px;background:var(--orange)}
.turbo p{position:absolute;left:76px;top:24px;font-size:24px;font-weight:600;color:#fff}
.site-footer{position:absolute;top:4578px;left:0;width:1200px;height:649px;background:var(--footer)}
.f-col{position:absolute;font-size:16px;line-height:31px;color:var(--footer-text)}
.f-col h5{font-size:17px;font-weight:500;color:#fff}
.contact-line{display:flex;gap:12px;align-items:flex-start;line-height:22px;margin-top:14px}
.footer-base{position:absolute;left:0;top:590px;width:1200px;border-top:1px solid #4a3d50;font-size:12px;color:var(--footer-text)}
.footer-base span{position:absolute;top:24px}
</style>
</head>
<body>

<header class="site-header">
  <div class="brand"><span class="dot"></span>quillmere</div>
  <nav class="utility-nav"><span>Blog</span><span>About Us</span><span>Contact Us</span><span>01632 960 000</span></nav>
  <nav class="main-nav"><span>Create</span><span>Communicate</span><span>Convert</span><span>Close</span><span>Case Studies</span></nav>
</header>

<section class="hero">
  <h1>Growth works<br>for you<em>in your targeting</em></h1>
  <div class="hero-art" role="img" aria-label="Illustration of a person riding a rocket past coins, a card and rising bar columns"></div>
</section>

<h2 class="intro-title">Fed Up With Agencies Who Don’t Care?<span>We’ve Heard That Before</span></h2>

<div class="pillar" style="left:67px">
  <svg width="56" height="56" viewBox="0 0 56 56" fill="none" stroke="#2a2230" stroke-width="1.6"><circle cx="24" cy="16" r="9"/><path d="M8 48c2-12 10-18 16-18s10 3 12 6"/><path d="M40 36l3 6 6 1-4 4 1 6-6-3-6 3 1-6-4-4 6-1z"/></svg>
  <b>We know every client has unique needs.</b> Yet, few digital agencies spend enough time getting to know the clients Business
</div>
<div class="pillar" style="left:427px">
  <svg width="56" height="56" viewBox="0 0 56 56" fill="none" stroke="#2a2230" stroke-width="1.6"><path d="M20 10l4 12 12 4-12 4-4 12-4-12-12-4 12-4z"/><path d="M42 6l2 6 6 2-6 2-2 6-2-6-6-2 6-2z"/><path d="M42 34l2 5 5 2-5 2-2 5-2-5-5-2 5-2z"/></svg>
  <b>We’re different.</b> We take a highly personalised approach to every project, working closely with our clients to understand their objectives, challenges and target audience
</div>
<div class="pillar" style="left:788px">
  <svg width="56" height="56" viewBox="0 0 56 56" fill="none" stroke="#2a2230" stroke-width="1.6"><circle cx="28" cy="12" r="7"/><circle cx="16" cy="32" r="6"/><circle cx="40" cy="32" r="6"/><path d="M6 52c1-8 5-12 10-12s9 4 10 12M30 52c1-8 5-12 10-12s9 4 10 12"/></svg>
  <b>Knowing your business</b> is the first step in helping you grow. It’s how we work, and it will work for you.
</div>

<section class="cta-band">
  <h2>Achieve Growth That Works</h2>
  <div class="btn" style="left:924px;top:23px;width:190px;height:54px">
    <svg width="16" height="16" viewBox="0 0 24 24" fill="#2a2230"><path d="M6.6 10.8a15 15 0 006.6 6.6l2.2-2.2a1 1 0 011-.25 11 11 0 003.5.56 1 1 0 011 1V20a1 1 0 01-1 1A17 17 0 013 4a1 1 0 011-1h3.5a1 1 0 011 1 11 11 0 00.56 3.5 1 1 0 01-.25 1z"/></svg>Set Up A Call
  </div>
</section>

<article class="service-card" style="left:67px;top:1468px">
  <span class="accent" style="background:var(--blue)"></span>
  <h3>Create</h3>
  <div class="service-item" style="left:38px;top:120px"><i style="background:#8fb1e8"></i>Branding</div>
  <div class="service-item" style="left:272px;top:120px"><i style="background:#e8a34a"></i>Graphics</div>
  <div class="service-item" style="left:38px;top:196px"><i style="background:#4a5ab8"></i>Video</div>
  <div class="service-item" style="left:272px;top:196px"><i style="background:#9fb7d6"></i>Content</div>
</article>
<article class="service-card" style="left:620px;top:1468px">
  <span class="accent" style="background:var(--orange)"></span>
  <h3>Communicate</h3>
  <div class="service-item" style="left:42px;top:120px"><i style="background:#e07a7a"></i>Ads</div>
  <div class="service-item" style="left:272px;top:120px"><i style="background:#f0a37a"></i>Organic</div>
  <div class="service-item" style="left:42px;top:196px"><i style="background:#4a8ad8"></i>Social</div>
  <div class="service-item" style="left:272px;top:196px"><i style="background:#5aa0e8"></i>Email</div>
</article>
<article class="service-card" style="left:67px;top:1803px">
  <span class="accent" style="background:var(--light-grey)"></span>
  <h3>Convert</h3>
  <div class="service-item" style="left:38px;top:112px"><i style="background:#6a9ad8;border-radius:50%"></i>Websites</div>
  <div class="service-item" style="left:272px;top:112px"><i style="background:#7ac27a"></i>Lead Generation</div>
  <div class="service-item" style="left:38px;top:214px"><i style="background:#e04a3a"></i>E-Commerce</div>
  <div class="service-item" style="left:272px;top:214px"><i style="background:#8aaee0"></i>Analytics</div>
</article>
<article class="service-card" style="left:620px;top:1803px">
  <span class="accent" style="background:var(--purple)"></span>
  <h3 style="left:52px">Close</h3>
  <div class="service-item" style="left:46px;top:112px"><i style="background:#f0b44a"></i>CRM</div>
  <div class="service-item" style="left:276px;top:112px"><i style="background:#4ab8c8;border-radius:50%"></i>Systems</div>
  <div class="service-item" style="left:46px;top:206px"><i style="background:#6a8ac8"></i>Customer<br>Success</div>
  <div class="service-item" style="left:276px;top:206px"><i style="background:#3a7ad8;border-radius:50%"></i>AI &amp;<br>Automations</div>
</article>

<div class="showcase-top">
  <span class="tag">WEBSITE</span>
  <svg class="abs" style="left:1006px;top:33px" width="18" height="18" viewBox="0 0 18 18" fill="#fff"><rect x="3" y="2" width="4" height="14" rx="1"/><rect x="11" y="2" width="4" height="14" rx="1"/></svg>
  <svg class="abs" style="left:1055px;top:30px" width="26" height="26" viewBox="0 0 26 26"><circle cx="13" cy="13" r="13" fill="#fff"/><path d="M10 8l8 5-8 5z" fill="#6a4fa8"/></svg>
</div>
<section class="showcase">
  <h3 style="left:108px">Your Pain?</h3>
  <p style="left:108px;width:370px">“I spend most of my development budget fixing errors and bugs”</p>
  <svg class="abs" style="left:522px;top:90px" width="46" height="40" viewBox="0 0 46 40" fill="none" stroke="#e27927" stroke-width="3.5" stroke-linecap="round" stroke-linejoin="round"><path d="M4 20h36M26 6l14 14-14 14"/></svg>
  <h3 style="left:625px">Future Gain</h3>
  <p style="left:625px;width:410px">A fast and reliable cash-generative content managed e-commerce or lead generation website</p>
</section>

<h2 class="about-title">Quillmere: <span>Where Growth Works</span></h2>
<ul class="about-list">
  <li><svg width="16" height="16" viewBox="0 0 16 16" fill="none" stroke="#2a2230" stroke-width="1.4"><rect x="1" y="3" width="14" height="9" rx="1"/><path d="M5 14h6"/></svg><span>We understand the importance of a strong online presence. That’s why we offer a complete range of digital marketing solutions to help your reach your growth goals.</span></li>
  <li><svg width="16" height="16" viewBox="0 0 16 16" fill="none" stroke="#2a2230" stroke-width="1.4"><path d="M8 1l6 2v5c0 4-3 6-6 7-3-1-6-3-6-7V3z"/><path d="M5 8l2 2 4-4"/></svg><span>Our track record demostartes expertise in all forms of digital marketing, including Website builds, Searchly Ads, SEO, Email Marketing.</span></li>
  <li><svg width="16" height="16" viewBox="0 0 16 16" fill="none" stroke="#2a2230" stroke-width="1.4"><rect x="1" y="3" width="14" height="12" rx="1"/><path d="M1 7h14M5 1v4M11 1v4"/></svg><span>We’re constantly staying up-to-date on the latest trends, tech and best practices in the industry, so you can trust that you’re getting the most effective and efficient stragies for your business growth.</span></li>
  <li><svg width="16" height="16" viewBox="0 0 24 24" fill="#2a2230"><path d="M6.6 10.8a15 15 0 006.6 6.6l2.2-2.2a1 1 0 011-.25 11 11 0 003.5.56 1 1 0 011 1V20a1 1 0 01-1 1A17 17 0 013 4a1 1 0 011-1h3.5a1 1 0 011 1 11 11 0 00.56 3.5 1 1 0 01-.25 1z"/></svg><span>Set up a call and we’re confident we can show you where we can add growth and value to your business.</span></li>
</ul>
<div class="about-art" role="img" aria-label="Illustration of a watering can feeding a potted money tree of coins"></div>

<section class="cases">
  <h2>Create<span>Case Studies</span></h2>
  <div class="case-card" style="left:76px"><span class="learn">Learn More <svg width="16" height="14" viewBox="0 0 16 14" fill="none" stroke="#e27927" stroke-width="2" stroke-linecap="round"><path d="M1 7h13M9 2l5 5-5 5"/></svg></span></div>
  <div class="case-card" style="left:340px"><span class="learn">Learn More <svg width="16" height="14" viewBox="0 0 16 14" fill="none" stroke="#e27927" stroke-width="2" stroke-linecap="round"><path d="M1 7h13M9 2l5 5-5 5"/></svg></span></div>
  <div class="case-card is-raised" style="left:603px"><span class="learn">Learn More <svg width="16" height="14" viewBox="0 0 16 14" fill="none" stroke="#e27927" stroke-width="2" stroke-linecap="round"><path d="M1 7h13M9 2l5 5-5 5"/></svg></span></div>
  <div class="case-card" style="left:866px"><span class="learn">Learn More <svg width="16" height="14" viewBox="0 0 16 14" fill="none" stroke="#e27927" stroke-width="2" stroke-linecap="round"><path d="M1 7h13M9 2l5 5-5 5"/></svg></span></div>
</section>

<h2 class="blog-title">From the Blog</h2>
<article class="blog-card" style="left:76px"><div class="thumb"></div><h4>Searchly’s New PPC Features are Loaded with AI</h4></article>
<article class="blog-card" style="left:340px"><div class="thumb"></div><h4>How Searchly Killed the Broad Match Keyword?</h4></article>
<article class="blog-card" style="left:603px"><div class="thumb"></div><h4>The 9 Rules of Social Media Engagement<br>(Part II)</h4></article>
<article class="blog-card" style="left:866px"><div class="thumb"></div><h4>The 9 Rules of Social Media Engagement<br>(Part I)</h4></article>

<section class="turbo">
  <p>We’re the turbo boost for your digital marketing engine</p>
  <div class="btn" style="left:860px;top:10px;width:258px;height:58px">Put Your Foot Down
    <svg width="16" height="16" viewBox="0 0 16 16" fill="none" stroke="#2a2230" stroke-width="1.5" stroke-linejoin="round"><path d="M15 1L1 7l6 2 2 6z"/></svg>
  </div>
</section>

<footer class="site-footer">
  <div class="f-col" style="left:74px;top:110px"><h5>Create</h5>Branding<br>Graphics<br>Video<br>Content</div>
  <div class="f-col" style="left:326px;top:110px"><h5>Convert</h5>Websites<br>Lead Generation<br>Ecommerce<br>Analytics</div>
  <div class="f-col" style="left:572px;top:110px"><h5>Connect</h5>Case Studies<br>Blog<br>About Us</div>
  <div class="f-col" style="left:804px;top:110px"><h5>Contact</h5>
    <div class="contact-line"><svg width="14" height="14" viewBox="0 0 24 24" fill="#a99bb0"><path d="M6.6 10.8a15 15 0 006.6 6.6l2.2-2.2a1 1 0 011-.25 11 11 0 003.5.56 1 1 0 011 1V20a1 1 0 01-1 1A17 17 0 013 4a1 1 0 011-1h3.5a1 1 0 011 1 11 11 0 00.56 3.5 1 1 0 01-.25 1z"/></svg>01632 960 000</div>
    <div class="contact-line" style="margin-top:30px"><svg width="14" height="16" viewBox="0 0 14 16" fill="none" stroke="#a99bb0" stroke-width="1.5"><path d="M7 15s5-5 5-9A5 5 0 002 6c0 4 5 9 5 9z"/><circle cx="7" cy="6" r="1.8"/></svg><span>Kestrel House, Aldbury<br>Northshire AB1 2CD</span></div>
  </div>
  <div class="f-col" style="left:74px;top:356px"><h5>Communicate</h5>Ads<br>Organic<br>Social<br>Email</div>
  <div class="f-col" style="left:326px;top:356px"><h5>Close</h5>CRM<br>Systems<br>Customer Success<br>AI &amp; Automations</div>
  <div class="footer-base">
    <span style="left:74px">(c) Quillmere Digital Limited. All rights reserved</span>
    <span style="left:740px">Sitemap</span>
    <span style="left:872px">Terms of Use</span>
    <span style="left:1003px">Privacy Policy</span>
  </div>
</footer>

</body>
</html>
```